Wine Label named: Amber Ridge

We are a wine producer, who wishes to launch a new premium wine called: Amber Ridge
Our winery is situated in a rolling hill, with slopes, where Amber Ridge exists in the property. One dates to the 15th century and the other more recent to the 18th century. Its a unique feature of the winery and we wish to create a label that represents these, but is NOT religious! Difficult task I know. Think you can pull it off? Let us see it! We start with one label, but the winner will have 5 more labels to design.

Target Market(s)

30-50 year old men

Industry/Entity Type

Wine

Colors

Designer to choose colors to be used in the design.

Requirements
Must have
• serious look and premium feel. name of the wine: Amber Ridge
Nice to have
• 2019 14% ABV
Should not have
• a religious look and feel

```html
<!DOCTYPE html>
<html lang="en">
<head>
<meta charset="utf-8">
<title>Amber Ridge — Wine Label</title>
<link rel="stylesheet" href="https://fonts.googleapis.com/css2?family=Pinyon+Script&family=Playfair+Display:wght@400&display=swap">
<style>
  :root {
    --backdrop: #d3d3d3;
    --paper: #f1f0ee;
    --ink: #1c1c1c;
    --wine-red: #7e0c12;
    --hill-light: #d9d9d9;
    --hill-dark: #3b3b3b;
  }
  html, body {
    margin: 0;
    padding: 0;
    overflow: hidden;
  }
  .canvas {
    width: 1200px;
    height: 1040px;
    background: var(--backdrop);
    display: flex;
    align-items: center;
    justify-content: center;
  }
  .wine-label {
    display: block;
    width: 556px;
    height: 960px;
  }
  .label-paper { fill: var(--paper); }
  .frame-line { fill: none; stroke: var(--ink); stroke-width: 2.2; }
  .rule-line { stroke: var(--ink); stroke-width: 2; }
  .tagline {
    font-family: "Pinyon Script", cursive;
    font-size: 52px;
    fill: var(--ink);
  }
  .name-caps {
    font-family: "Playfair Display", serif;
    font-size: 62px;
    letter-spacing: 2px;
    fill: var(--ink);
  }
  .name-script {
    font-family: "Pinyon Script", cursive;
    font-size: 170px;
    fill: var(--wine-red);
  }
  .vintage {
    font-family: "Playfair Display", serif;
    font-size: 70px;
    font-variant-numeric: lining-nums;
    fill: var(--wine-red);
  }
  .strength {
    font-family: "Playfair Display", serif;
    font-size: 28px;
    letter-spacing: 1px;
    font-variant-numeric: lining-nums;
    fill: var(--ink);
  }
</style>
</head>
<body>
<main class="canvas">
  <svg class="wine-label" viewBox="0 0 858 1480" xmlns="http://www.w3.org/2000/svg">
    <defs>
      <path id="tagline-arc" d="M255,190 Q430,90 610,200"/>
      <linearGradient id="hill-tones" x1="0" y1="0" x2="0" y2="1">
        <stop offset="0" stop-color="var(--hill-light)"/>
        <stop offset="0.45" stop-color="#6a6a6a"/>
        <stop offset="1" stop-color="var(--hill-dark)"/>
      </linearGradient>
    </defs>

    <rect class="label-paper" x="0" y="0" width="858" height="1480"/>

    <!-- frame -->
    <path class="frame-line" d="M98,820 L98,207 L140,207 Q200,200 212,150 Q270,82 430,80 Q590,82 645,150 Q660,200 720,207 L760,207 L760,820"/>
    <path class="frame-line" d="M98,1062 L98,1277 L140,1277 Q200,1284 212,1334 Q270,1396 430,1398 Q590,1396 645,1334 Q660,1284 720,1277 L760,1277 L760,1062"/>

    <text class="tagline"><textPath href="#tagline-arc" startOffset="50%" text-anchor="middle">Premium Quality</textPath></text>

    <!-- wine name -->
    <text class="name-caps" x="585" y="388" text-anchor="middle">AMBER</text>
    <text class="name-script" x="420" y="540" text-anchor="middle">Ridge</text>

    <rect x="96" y="632" width="666" height="410" fill="url(#hill-tones)" role="img" aria-label="Pencil-shaded drawing of rolling vineyard hills with two old stone buildings on the crests"/>

    <!-- vintage -->
    <g class="vintage-rules">
      <line class="rule-line" x1="232" y1="1126" x2="362" y2="1126"/>
      <line class="rule-line" x1="205" y1="1140" x2="362" y2="1140"/>
      <line class="rule-line" x1="232" y1="1154" x2="362" y2="1154"/>
      <line class="rule-line" x1="502" y1="1126" x2="632" y2="1126"/>
      <line class="rule-line" x1="502" y1="1140" x2="660" y2="1140"/>
      <line class="rule-line" x1="502" y1="1154" x2="632" y2="1154"/>
    </g>
    <text class="vintage" x="432" y="1165" text-anchor="middle" textLength="122" lengthAdjust="spacingAndGlyphs">2019</text>

    <text class="strength" x="428" y="1276" text-anchor="middle">14% ABV</text>
  </svg>
</main>
</body>
</html>
```